TalkBloom - Language Coaching Services

Sleek, innovative, trendy design for Language Coaching business.

TalkBloom is a new UK based company that provides Language Coaching services. We offer highly personalized on-line and face to face language courses. We also impart learning techniques workshops based on the latest neuroscience research for second-language acquisition.

Target Market(s)

Industry/Entity Type

Consulting

Contact Information for Business Card

TalkBloom
DaniraQT@talkbloom.co.uk
TalkBloom.co.uk
London, UK

Font styles to use
Sans Serif

```html
<!DOCTYPE html>
<html lang="en">
<head>
<meta charset="utf-8">
<title>TalkBloom – Business Cards</title>
<link rel="stylesheet" href="https://fonts.googleapis.com/css2?family=Montserrat:wght@300;500&family=Arimo:wght@400;700&display=swap">
<style>
  :root {
    --backdrop: #2b2b2d;
    --teal-light: #1f7893;
    --teal-dark: #14586e;
    --card-white: #f7f7f6;
    --ink-blue: #1d5f86;
    --logo-blue: #1f7ea3;
    --ink-dark: #1e1e1e;
    --on-teal: #e9f2f5;
  }
  * { margin: 0; padding: 0; box-sizing: border-box; }
  html, body {
    width: 1200px; height: 997px; overflow: hidden;
    background: var(--backdrop);
  }
  .stage {
    position: relative; width: 1200px; height: 997px;
  }
  .card {
    position: absolute; left: 280px; width: 640px; height: 366px;
    border-radius: 2px;
    box-shadow: 0 14px 30px rgba(0,0,0,.45);
  }
  .card--front {
    top: 110px;
    background: linear-gradient(160deg, var(--teal-light), var(--teal-dark));
  }
  .card--back {
    top: 520px;
    background: var(--card-white);
  }
  .brand {
    position: absolute; left: 0; right: 0;
    display: flex; flex-direction: column; align-items: center;
  }
  .card--front .brand { top: 62px; }
  .card--back .brand { top: 30px; }
  .brand__circle {
    border-radius: 50%; border-style: solid;
  }
  .card--front .brand__circle {
    width: 120px; height: 120px; border: 9px solid var(--on-teal);
  }
  .card--back .brand__circle {
    width: 82px; height: 82px; border: 6px solid var(--logo-blue);
  }
  .brand__name {
    font-family: "Montserrat", sans-serif; font-weight: 500;
    text-transform: uppercase; letter-spacing: 2px; line-height: 1;
  }
  .card--front .brand__name {
    margin-top: 26px; font-size: 62px; color: var(--on-teal);
  }
  .card--back .brand__name {
    margin-top: 16px; font-size: 42px; color: var(--logo-blue);
  }
  .rule {
    position: absolute; height: 2px; background: var(--ink-blue);
  }
  .rule--long { left: 110px; right: 40px; top: 196px; }
  .person {
    position: absolute; left: 40px; top: 200px;
    font-family: "Arimo", sans-serif;
  }
  .person__name {
    font-weight: 700; font-size: 17px; color: var(--ink-blue);
    letter-spacing: .5px; text-transform: uppercase;
  }
  .person__role { font-size: 13px; color: var(--ink-dark); margin-top: 1px; }
  .contacts {
    position: absolute; left: 40px; top: 252px; list-style: none;
    font-family: "Montserrat", sans-serif; font-size: 15px; color: var(--ink-dark);
  }
  .contacts li {
    display: flex; align-items: center; gap: 10px; height: 28px;
  }
  .contacts svg { width: 20px; height: 20px; flex: none; }
  .website {
    position: absolute; right: 40px; top: 210px;
    font-family: "Arimo", sans-serif; font-weight: 700;
    font-size: 15px; color: var(--ink-blue);
  }
</style>
</head>
<body>
<main class="stage">
  <section class="card card--front" aria-label="Business card front">
    <div class="brand">
      <div class="brand__circle"></div>
      <div class="brand__name">TalkBloom</div>
    </div>
  </section>

  <section class="card card--back" aria-label="Business card back">
    <div class="brand">
      <div class="brand__circle"></div>
      <div class="brand__name">TalkBloom</div>
    </div>
    <div class="rule rule--long"></div>
    <div class="person">
      <div class="person__name">Imogen Hartley</div>
      <div class="person__role">Director</div>
    </div>
    <div class="website">www.talkbloom.co.uk</div>
    <ul class="contacts">
      <li>
        <svg viewBox="0 0 20 20" aria-hidden="true"><circle cx="10" cy="10" r="10" fill="#1d5f86"/><path d="M7 5.5l2 2-1 1.3c.6 1.3 1.6 2.3 2.9 2.9l1.3-1 2 2-1.2 1.5c-3.6-.3-6.8-3.5-7-7z" fill="#fff"/></svg>
        020.7946.0382
      </li>
      <li>
        <svg viewBox="0 0 20 20" aria-hidden="true"><circle cx="10" cy="10" r="10" fill="#1d5f86"/><rect x="5" y="6.5" width="10" height="7" fill="none" stroke="#fff" stroke-width="1.2"/><path d="M5 6.5l5 4 5-4" fill="none" stroke="#fff" stroke-width="1.2"/></svg>
        DaniraQT@talkbloom.co.uk
      </li>
      <li>
        <svg viewBox="0 0 20 20" aria-hidden="true"><circle cx="10" cy="10" r="10" fill="#1d5f86"/><path d="M10 4.5a3.5 3.5 0 0 0-3.5 3.5c0 2.6 3.5 7 3.5 7s3.5-4.4 3.5-7A3.5 3.5 0 0 0 10 4.5z" fill="#fff"/><circle cx="10" cy="8" r="1.3" fill="#1d5f86"/></svg>
        London, UK
      </li>
    </ul>
  </section>
</main>
</body>
</html>
```